Fabric Softener

We need fabric softener. Bottle picture attached for reference. Color of bottle can be proposed as well. Normally bottle is pink and blue color

Logo is also attached that shall be used.
Updates

Need extra days to review

Low designer entries

Target Market(s)

Niche

Font styles to use
Sans Serif

Requirements
Must have
• Fabric, Brightness, Nature
Nice to have
• Good colors
Should not have
• Adults

```html
<!DOCTYPE html>
<html lang="en">
<head>
<meta charset="utf-8">
<title>Plumera Super Softener – Label</title>
<link rel="stylesheet" href="https://fonts.googleapis.com/css2?family=Lilita+One&family=Roboto+Condensed:wght@400;700&display=swap">
<style>
  :root {
    --page-bg: #f4f5f6;
    --sky-light: #e4f4fd;
    --sky-mid: #8fd0f2;
    --sky-deep: #5fb6ea;
    --band-light: #4aa9e6;
    --band-deep: #2386e0;
    --brand-blue: #2287de;
    --ink-navy: #0e3f8f;
    --cream: #fffbe6;
    --pink: #ee6f9f;
    --white: #ffffff;
  }
  * { margin: 0; padding: 0; box-sizing: border-box; }
  html, body { width: 1200px; height: 905px; overflow: hidden; }
  body { background: var(--page-bg); position: relative; }
  .softener-label {
    position: absolute;
    left: 360px;
    top: 125px;
    width: 480px;
    height: 654px;
    display: block;
  }
  .brand-name {
    font-family: "Roboto Condensed", sans-serif;
    font-weight: 700;
    font-size: 78px;
    fill: var(--white);
  }
  .headline {
    font-family: "Lilita One", sans-serif;
    fill: var(--ink-navy);
    stroke: var(--cream);
    stroke-width: 6px;
    paint-order: stroke fill;
  }
  .new-tag-text {
    font-family: "Roboto Condensed", sans-serif;
    font-weight: 700;
    font-size: 22px;
    fill: var(--white);
  }
  .loads-title {
    font-family: "Roboto Condensed", sans-serif;
    font-weight: 700;
    font-size: 34px;
    fill: var(--white);
  }
  .loads-detail {
    font-family: "Roboto Condensed", sans-serif;
    font-weight: 700;
    font-size: 24px;
    fill: var(--white);
  }
  .badge-number {
    font-family: "Roboto Condensed", sans-serif;
    font-weight: 700;
    font-size: 50px;
    fill: var(--brand-blue);
  }
  .badge-caption {
    font-family: "Roboto Condensed", sans-serif;
    font-weight: 700;
    font-size: 16px;
    fill: var(--brand-blue);
  }
</style>
</head>
<body>
  <svg class="softener-label" viewBox="0 0 690 940" xmlns="http://www.w3.org/2000/svg" aria-label="Plumera Super Softener label">
    <defs>
      <linearGradient id="skyFill" x1="0" y1="0" x2="0.4" y2="1">
        <stop offset="0" stop-color="var(--sky-light)"/>
        <stop offset="0.45" stop-color="var(--sky-mid)"/>
        <stop offset="1" stop-color="var(--sky-deep)"/>
      </linearGradient>
      <linearGradient id="bandFill" x1="0" y1="0" x2="1" y2="0.3">
        <stop offset="0" stop-color="var(--band-light)"/>
        <stop offset="1" stop-color="var(--band-deep)"/>
      </linearGradient>
      <radialGradient id="fabricGlow" cx="0.5" cy="0.5" r="0.5">
        <stop offset="0" stop-color="#ffffff" stop-opacity="0.95"/>
        <stop offset="0.6" stop-color="#eef7fd" stop-opacity="0.7"/>
        <stop offset="1" stop-color="#bfe4f8" stop-opacity="0"/>
      </radialGradient>
      <clipPath id="labelShape">
        <path d="M0,300 C0,120 60,0 170,0 C260,0 290,80 330,200 L620,560 C660,610 690,640 690,700 L690,860 C690,910 660,940 620,940 L80,940 C30,940 0,900 0,850 Z"/>
      </clipPath>
    </defs>

    <g clip-path="url(#labelShape)">
      <rect class="label-sky" width="690" height="940" fill="url(#skyFill)"/>

      <ellipse class="fabric-illustration" role="img" aria-label="White t-shirt wrapped in a glowing swirl with pink petals and bubbles"
               cx="360" cy="590" rx="260" ry="210" fill="url(#fabricGlow)"/>

      <path class="wave-band" d="M0,790 C120,740 240,750 420,800 C540,830 620,810 690,770 L690,940 L0,940 Z" fill="url(#bandFill)"/>
      <path class="wave-line" d="M0,790 C120,740 240,750 420,800 C540,830 620,810 690,770" fill="none" stroke="var(--white)" stroke-width="6"/>
    </g>

    <g class="brand-mark">
      <circle cx="60" cy="225" r="14" fill="var(--brand-blue)"/>
      <text class="brand-name" x="82" y="250" fill="var(--brand-blue)" style="fill: var(--brand-blue)">Plumera</text>
    </g>

    <g class="product-headline" transform="rotate(-8 330 400)">
      <text class="headline" x="80" y="380" font-size="76">SUPER</text>
      <text class="headline" x="10" y="470" font-size="92">SOFTENER</text>
      <g class="new-tag" transform="translate(265 302)">
        <polygon points="0,8 72,0 80,24 72,34 0,42" fill="var(--pink)"/>
        <text class="new-tag-text" x="12" y="30">NEW</text>
      </g>
    </g>

    <g class="pack-size">
      <text class="loads-title" x="150" y="842">120 LOADS</text>
      <text class="loads-detail" x="150" y="872">130 FL OZ</text>
      <text class="loads-detail" x="150" y="902">(1.05 GAL) 3.99L</text>
    </g>

    <g class="freshness-badge" transform="translate(540 800) rotate(-4)">
      <polygon fill="var(--white)" stroke="var(--brand-blue)" stroke-width="2"
        points="70,0 58.8,11.7 64.7,26.8 49.9,33.3 49.5,49.5 33.3,49.9 26.8,64.7 11.7,58.8 0,70 -11.7,58.8 -26.8,64.7 -33.3,49.9 -49.5,49.5 -49.9,33.3 -64.7,26.8 -58.8,11.7 -70,0 -58.8,-11.7 -64.7,-26.8 -49.9,-33.3 -49.5,-49.5 -33.3,-49.9 -26.8,-64.7 -11.7,-58.8 0,-70 11.7,-58.8 26.8,-64.7 33.3,-49.9 49.5,-49.5 49.9,-33.3 64.7,-26.8 58.8,-11.7"/>
      <text class="badge-number" x="0" y="2" text-anchor="middle">30</text>
      <text class="badge-caption" x="0" y="24" text-anchor="middle">DAYS OF</text>
      <text class="badge-caption" x="0" y="41" text-anchor="middle">FRESHNESS</text>
    </g>
  </svg>
</body>
</html>
```